Stationery for a recruitment agency

We need a logo, letterhead and business card design that will represent our 28 year old recruitment agency that was started by us in 1989 here in Perth (Australia). We target professional companies that want us to do their sourcing and screening of candidates.

Primarily our clients like to use agencies as we have greater access to candidates than they do. Our imagery needs to reflect strength and that we are serious about recruiting and systems, and that we can meet their people supply needs both now and into the future.

Once we place a person into a job we also help manage their performance as we do Performance Appraisals and link the goals of the company to the KPI's (Key Performance Indicators) of the individual.

Target Market(s)

Corporate companies with 50+ employees

Industry/Entity Type

Recruitment

Font styles to use
Serif
Sans Serif

Colors

Designer to choose colors to be used in the design.

Requirements
Must have
• Our business name is Harbor Staffing and must be used in the logo
Nice to have
• Having been around since 1989 is a pretty big thing in such a competitive business.

```html
<!DOCTYPE html>
<html lang="en">
<head>
<meta charset="utf-8">
<title>Harbor Staffing Letterhead</title>
<link href="https://fonts.googleapis.com/css2?family=Cinzel:wght@500;600&family=Lato:wght@400&family=Great+Vibes&display=swap" rel="stylesheet">
<style>
  :root {
    --brand-blue: #0a4f9e;
    --brand-grey: #7b7d80;
    --ink: #1f1f1f;
    --muted-ink: #444;
    --paper: #f7f7f7;
    --backdrop: #d9d9d9;
  }
  html, body {
    margin: 0;
    width: 1200px;
    height: 1048px;
    overflow: hidden;
    background: var(--backdrop);
  }
  .letterhead {
    position: absolute;
    left: 243px;
    top: 16px;
    width: 595px;
    height: 846px;
    background: var(--paper);
    transform: scale(1.2);
    transform-origin: top left;
    font-family: "Lato", sans-serif;
    color: var(--ink);
    overflow: hidden;
  }
  .header-bands { position: absolute; left: 0; top: 0; }
  .brand-name {
    position: absolute;
    left: 48px;
    top: 68px;
    display: flex;
    align-items: center;
    gap: 8px;
    font-family: "Cinzel", serif;
    font-weight: 600;
    font-size: 22px;
    line-height: 26px;
    color: var(--brand-blue);
    letter-spacing: 0.5px;
  }
  .brand-mark {
    width: 12px;
    height: 12px;
    background: var(--brand-blue);
  }
  .sender {
    position: absolute;
    right: 47px;
    top: 65px;
    text-align: right;
    font-style: normal;
    font-size: 8px;
    line-height: 11px;
  }
  .sender-name {
    font-family: "Cinzel", serif;
    font-weight: 500;
    font-size: 11px;
    color: var(--brand-blue);
    margin-bottom: 1px;
  }
  .recipient {
    position: absolute;
    left: 44px;
    top: 224px;
    font-size: 11.5px;
    line-height: 15px;
  }
  .salutation {
    position: absolute;
    left: 44px;
    top: 307px;
    font-size: 13px;
  }
  .body-copy {
    position: absolute;
    left: 44px;
    top: 335px;
    width: 503px;
    font-size: 9.4px;
    line-height: 13px;
    text-align: justify;
    hyphens: auto;
  }
  .body-copy p { margin: 0 0 13px; }
  .body-copy p.tight { margin-bottom: 7px; }
  .closing {
    position: absolute;
    left: 44px;
    top: 600px;
    font-size: 10px;
  }
  .signatory {
    font-family: "Great Vibes", cursive;
    font-size: 22px;
    color: var(--brand-blue);
    margin-top: 2px;
  }
  .contact-bar {
    position: absolute;
    left: 0;
    right: 0;
    top: 806px;
    display: flex;
    justify-content: center;
    gap: 10px;
    font-size: 9px;
    color: var(--muted-ink);
  }
  .contact-item { display: flex; align-items: center; gap: 5px; }
  .contact-item svg { width: 9px; height: 9px; fill: var(--brand-blue); }
</style>
</head>
<body>
  <main class="letterhead">
    <svg class="header-bands" width="595" height="70" viewBox="0 0 595 70" aria-hidden="true">
      <polygon points="240,0 595,0 595,38 410,20" fill="var(--brand-grey)"/>
      <polygon points="0,0 240,0 410,20 0,65" fill="var(--brand-blue)"/>
    </svg>

    <div class="brand-name"><span class="brand-mark"></span>Harbor Staffing</div>

    <address class="sender">
      <div class="sender-name">Harbor Staffing</div>
      <div>88 Quayside Rd Unit 12</div>
      <div>Fremantle, WA 6160</div>
    </address>

    <div class="recipient">
      <div>Mr/s</div>
      <div>First &amp; Last name</div>
      <div>Company nmae</div>
      <div>Address</div>
    </div>

    <div class="salutation">Dear Sir</div>

    <div class="body-copy">
      <p>Lorem Ipsum is simply dummy text of the printing and typesetting industry. Lorem Ipsum has been the indus&shy;try's standard dummy text ever since the 1500s, when an unknown printer took a galley of type and scrambled it to make a type specimen book. I It was popularised in the 1960s with the release of Presstype sheets containing Lorem Ipsum passages, and more recently with desktop publishing software like Folio</p>
      <p>It is a long established fact that a reader will be distracted by the readable content of a page when looking at its layout. The point of using Lorem Ipsum is that it has a more-or-less normal distribution of letters, as opposed to using 'Content here, content here', making it look like readable English. It is a long established fact etters, as opposed to using &nbsp;that a reader will be etters, as opposed to using &nbsp;distracted by the readable</p>
      <p class="tight">The point of using Lorem Ipsum is that it has a more-or-less normal distribution of letters, as opposed to using 'Content here, content here', making it look like readable English. page editors now use Lorem Ipsum as their default model text, and a search for 'lorem ipsum' will uncover many web sites still in their infancy. Various versions have evolved over the years, sometimes by accident, sometimes on purpose (injected humour and the like. English. page editors now use Lorem Ipsum as their default model text, and a search for 'lorem ipsum'</p>
      <p>It is a long established fact that a reader will be distracted by the readable content of a page when looking at its layout. The point of using Lorem Ipsum is that it has a more-or-less normal distribution of letters, as opposed to using 'Content here, content here', making it look like readable English. I</p>
    </div>

    <div class="closing">
      <div>Warm regards</div>
      <div class="signatory">Ellis</div>
    </div>

    <footer class="contact-bar">
      <span class="contact-item">
        <svg viewBox="0 0 10 10" aria-hidden="true"><path d="M2 0.5 L4 2.8 L3 4 Q4.2 6 6 7 L7.2 6 L9.5 8 L8.3 9.5 Q3.5 9 0.5 1.7 Z"/></svg>
        08.5550.1989
      </span>
      <span class="contact-item">
        <svg viewBox="0 0 10 10" aria-hidden="true"><path d="M0 2 H10 V8.5 H0 Z M0.8 2.6 L5 5.6 L9.2 2.6" stroke="#fff" stroke-width="0.8"/></svg>
        info@HarborStaffing.com
      </span>
      <span class="contact-item">
        <svg viewBox="0 0 10 10" aria-hidden="true"><circle cx="5" cy="5" r="4.6"/><path d="M0.5 5 H9.5 M5 0.5 V9.5 M5 0.5 Q2 5 5 9.5 M5 0.5 Q8 5 5 9.5" stroke="#fff" stroke-width="0.6" fill="none"/></svg>
        www.HarborStaffing.com
      </span>
    </footer>
  </main>
</body>
</html>
```